CCTV Website

We are looking for a Wordpress designer to create an e-commerce website for us. We have all the products that will be uploaded to site on csv format, so our main focus is layout, style, home page slider image selections and related site page images selection by the designer.

When project is reaching completion we will provide product files.

Industry/Entity Type

E-Commerce

```html
<!DOCTYPE html>
<html lang="en">
<head>
<meta charset="utf-8">
<title>Kestrel Securities — CCTV Services</title>
<link href="https://fonts.googleapis.com/css2?family=Roboto:wght@400;500;700;900&family=Open+Sans:wght@400;600&display=swap" rel="stylesheet">
<style>
:root{
  --red:#d7242b;
  --red-dark:#b81c22;
  --navy:#1f2a44;
  --navy-deep:#18213a;
  --ink:#222;
  --text:#555;
  --light:#f5f5f5;
  --line:#ddd;
  --white:#fff;
}
*{box-sizing:border-box;margin:0;padding:0}
html,body{width:1200px;height:3087px;overflow:hidden}
body{font-family:"Open Sans",Arial,sans-serif;color:var(--text);background:var(--white);position:relative;font-size:12px;line-height:1.9}
h1,h2,h3,h4,.nav,.btn{font-family:"Roboto",Arial,sans-serif}
.abs{position:absolute}
.btn{display:inline-block;background:var(--red);color:var(--white);font-weight:700;font-size:13px;text-transform:uppercase;text-align:center;border-radius:3px}

/* header */
.site-header{position:absolute;left:0;top:0;width:1200px;height:115px;background:var(--white)}
.brand{position:absolute;left:100px;top:22px;display:flex;align-items:center;gap:12px}
.brand-mark{width:60px;height:60px;background:var(--red);border-radius:4px}
.brand-name{font-family:"Roboto",sans-serif;font-weight:700;font-size:24px;line-height:1.05;color:var(--navy);text-transform:uppercase}
.header-phone{position:absolute;left:690px;top:22px;font-family:"Roboto",sans-serif;font-size:21px;color:var(--ink);display:flex;align-items:center;gap:12px}
.header-cta{position:absolute;left:930px;top:18px;width:172px;height:36px;line-height:36px;font-size:13px}
.nav{position:absolute;right:98px;top:76px;display:flex;gap:30px;font-size:15px;font-weight:500;color:var(--ink);text-transform:uppercase;letter-spacing:.3px}

/* hero */
.hero{position:absolute;left:0;top:115px;width:1200px;height:580px;background:linear-gradient(120deg,#aebfd0 0%,#d7e2ec 45%,#9fb3c6 100%)}
.hero-photo{position:absolute;inset:0;background:linear-gradient(135deg,#8a9098 0%,#c9d2da 30%,#e3eaf0 55%,#a9bccd 100%)}
.hero-title{position:absolute;left:295px;top:362px;font-family:"Roboto",sans-serif;font-weight:900;font-size:40px;line-height:1.3;color:var(--white);text-align:center;text-transform:uppercase;text-shadow:0 0 3px #111,2px 2px 0 #222}
.slider-arrow{position:absolute;top:292px;width:32px;height:32px;border-radius:50%;background:rgba(40,40,40,.75);display:flex;align-items:center;justify-content:center}
.quote-panel{position:absolute;left:770px;top:100px;width:328px;height:375px;background:var(--navy);border:4px solid #c7cfdd;padding:26px 22px;text-align:center;color:var(--white)}
.quote-panel h3{font-size:22px;font-weight:700;line-height:1.2}
.quote-panel p{font-family:"Roboto",sans-serif;font-weight:700;font-size:16px;margin-bottom:14px}
.field{height:38px;background:var(--white);margin-bottom:10px;text-align:left;padding:0 12px;font-size:12px;line-height:38px;color:#333}
.quote-panel .btn{width:100%;height:42px;line-height:42px;font-size:15px;font-weight:500;background:#e94a35;margin-top:4px}

/* services */
.services{position:absolute;left:0;top:695px;width:1200px;height:515px;background:var(--light)}
.section-title{font-family:"Roboto",sans-serif;font-weight:500;font-size:34px;color:var(--ink);text-transform:uppercase;text-align:center}
.service{position:absolute;top:130px;width:320px;text-align:center}
.service-icon{width:124px;height:124px;margin:0 auto 16px}
.service h4{font-size:17px;font-weight:500;color:var(--ink);text-transform:uppercase;margin-bottom:8px}
.service p{font-size:11.5px;line-height:1.95}
.btn-outline{display:inline-block;margin-top:16px;border:1.5px solid #444;border-radius:14px;padding:0 10px;height:28px;line-height:25px;font-family:"Roboto",sans-serif;font-size:11px;font-weight:500;color:#333;text-transform:uppercase}

/* about */
.about-frame{position:absolute;left:108px;top:1302px;width:455px;height:325px;border:2px solid var(--red)}
.about-photo{position:absolute;left:98px;top:1312px;width:455px;height:332px;background:linear-gradient(135deg,#2d3c52,#6f8aa6 45%,#d6dde6 70%,#9aa6b3);}
.copy h2{font-family:"Roboto",sans-serif;font-weight:500;font-size:32px;color:var(--ink);text-transform:uppercase;margin-bottom:18px}
.copy p{font-size:12px;line-height:2.15;margin-bottom:12px}
.copy .btn{width:142px;height:36px;line-height:36px;margin-top:10px}
.checklist{list-style:none;margin:8px 0 18px}
.checklist li{font-size:12px;line-height:2.15;display:flex;align-items:center;gap:10px}

/* monitor */
.monitor-screen{position:absolute;left:690px;top:1757px;width:410px;height:268px;background:#111;border-radius:8px;padding:14px}
.monitor-screen div{width:100%;height:100%;background:linear-gradient(135deg,#1e3a5c,#4a7aa8 50%,#c6d0da)}
.monitor-chin{position:absolute;left:690px;top:2025px;width:410px;height:38px;background:linear-gradient(#f4f4f4,#d9d9d9);border-radius:0 0 8px 8px}
.monitor-stand{position:absolute;left:840px;top:2063px;width:110px;height:30px;background:linear-gradient(#cfcfcf,#eee);clip-path:polygon(20% 0,80% 0,100% 100%,0 100%)}

/* blog */
.blog{position:absolute;left:0;top:2172px;width:1200px;height:548px;background:linear-gradient(120deg,var(--navy-deep),#2a3a5c 60%,#1c2741)}
.blog .section-title{color:var(--white);margin-top:58px}
.blog-card{position:absolute;top:158px;width:313px;height:308px;background:var(--white)}
.blog-thumb{height:175px}
.blog-body{padding:14px 16px}
.blog-body h4{font-family:"Open Sans",sans-serif;font-weight:400;font-size:14px;color:#333;margin-bottom:4px}
.blog-meta{font-size:11.5px;color:#444;display:flex;align-items:center;gap:6px;margin-bottom:6px}
.blog-body p{font-size:11px;line-height:1.9}

/* footer */
.site-footer{position:absolute;left:0;top:2720px;width:1200px;height:310px;background:var(--light)}
.footer-col{position:absolute;top:52px}
.footer-col h4{font-size:18px;font-weight:500;color:var(--ink);text-transform:uppercase;margin-bottom:14px}
.footer-col p,.footer-col li{font-size:11.5px;line-height:1.75;color:#444}
.newsletter-input{width:268px;height:40px;border:1px solid var(--line);background:var(--white);margin:14px 0 12px;padding-left:12px;line-height:40px;font-size:11px;color:#444}
.newsletter-btn{width:120px;height:32px;line-height:32px;font-size:12px;font-weight:500}
.contact-line{display:flex;gap:10px;align-items:flex-start;margin-bottom:12px}
.quick-links{list-style:none}
.socials{display:flex;gap:6px;margin-top:26px}
.socials span{width:26px;height:26px;border:1.5px solid #333;border-radius:50%}
.footer-bar{position:absolute;left:0;top:3030px;width:1200px;height:57px;border-top:1px solid var(--line);text-align:center;line-height:57px;font-size:11.5px;color:#333}
</style>
</head>
<body>

<header class="site-header">
  <div class="brand"><span class="brand-mark"></span><span class="brand-name">Kestrel<br>Securities</span></div>
  <div class="header-phone">
    <svg width="22" height="22" viewBox="0 0 24 24"><path fill="#222" d="M6.6 10.8a15.1 15.1 0 0 0 6.6 6.6l2.2-2.2c.3-.3.7-.4 1-.2 1.1.4 2.3.6 3.6.6.6 0 1 .4 1 1V20c0 .6-.4 1-1 1A17 17 0 0 1 3 4c0-.6.4-1 1-1h3.5c.6 0 1 .4 1 1 0 1.3.2 2.5.6 3.6.1.3 0 .7-.2 1z"/></svg>
    +1 800 555 0142
  </div>
  <span class="btn header-cta">Book Online Now</span>
  <nav class="nav"><span>Home</span><span>About Us</span><span>Our Services</span><span>Blog</span><span>Contact Us</span></nav>
</header>

<section class="hero">
  <div class="hero-photo" role="img" aria-label="Security camera mounted on an arm in front of a blurred glass office building"></div>
  <h1 class="hero-title">Kestrel Securities<br>CCTV Services</h1>
  <span class="slider-arrow" style="left:40px"><svg width="12" height="12" viewBox="0 0 12 12"><path d="M8 1 3 6l5 5" stroke="#fff" stroke-width="2" fill="none"/></svg></span>
  <span class="slider-arrow" style="left:1136px"><svg width="12" height="12" viewBox="0 0 12 12"><path d="M4 1l5 5-5 5" stroke="#fff" stroke-width="2" fill="none"/></svg></span>
  <form class="quote-panel">
    <h3>REQUEST A FREE QUOTE</h3>
    <p>or Call us +1 800 555 0142</p>
    <div class="field">First Name *</div>
    <div class="field">Email *</div>
    <div class="field">Phone Number *</div>
    <div class="field">How Can We Help?</div>
    <div class="btn">Request a Free Quote</div>
  </form>
</section>

<section class="services">
  <h2 class="section-title" style="margin-top:62px">CCTV Services</h2>
  <div class="service" style="left:80px">
    <svg class="service-icon" viewBox="0 0 124 124"><path d="M62 4a58 58 0 1 1-41 17" fill="none" stroke="#1f2a44" stroke-width="4"/><circle cx="62" cy="62" r="50" fill="#d7242b"/><path d="M62 36 36 58h7v26h14V70h10v14h14V58h7z" fill="none" stroke="#fff" stroke-width="4" stroke-linejoin="round"/></svg>
    <h4>Residential</h4>
    <p>Sed ut perspiciatis unde omnis iste natus error sit voluptatem accusantium doloremque laudantium, totam rem aperiam, eaque ipsa quae ab illo inventore veritatis et quasi architecto beatae</p>
    <span class="btn-outline">Read More ⊛</span>
  </div>
  <div class="service" style="left:440px">
    <svg class="service-icon" viewBox="0 0 124 124"><path d="M62 4a58 58 0 1 1-41 17" fill="none" stroke="#1f2a44" stroke-width="4"/><circle cx="62" cy="62" r="50" fill="#d7242b"/><rect x="40" y="48" width="36" height="16" rx="3" fill="#fff"/><rect x="76" y="52" width="8" height="8" fill="#fff"/><path d="M58 64v12H44" stroke="#fff" stroke-width="4" fill="none"/></svg>
    <h4>Corporate Customers</h4>
    <p>Sed ut perspiciatis unde omnis iste natus error sit voluptatem accusantium doloremque laudantium, totam rem aperiam, eaque ipsa quae ab illo inventore veritatis et quasi architecto beatae</p>
    <span class="btn-outline">Read More ⊛</span>
  </div>
  <div class="service" style="left:792px">
    <svg class="service-icon" viewBox="0 0 124 124"><path d="M62 4a58 58 0 1 1-41 17" fill="none" stroke="#1f2a44" stroke-width="4"/><circle cx="62" cy="62" r="50" fill="#d7242b"/><path d="M62 34 40 42v16c0 15 9 26 22 31 13-5 22-16 22-31V42z" fill="#fff"/><path d="m52 62 7 7 13-14" stroke="#d7242b" stroke-width="4" fill="none"/></svg>
    <h4>Information Security</h4>
    <p>Sed ut perspiciatis unde omnis iste natus error sit voluptatem accusantium doloremque laudantium, totam rem aperiam, eaque ipsa quae ab illo inventore veritatis et quasi architecto beatae</p>
    <span class="btn-outline">Read More ⊛</span>
  </div>
</section>

<div class="about-frame"></div>
<div class="about-photo" role="img" aria-label="Security operator at a desk watching several CCTV monitors"></div>
<section class="copy abs" style="left:622px;top:1306px;width:480px">
  <h2>About Kestrel Securities</h2>
  <p>Sed ut perspiciatis unde omnis iste natus error sit voluptatem accusantium loremque laudantium, totam rem aperiam, eaque ipsa quae ab illo inventore veritatis et quasi architecto beatae vitae dicta sunt explicabo. Nemo enim ipsam voluptatem quia voluptas sit aspernatur aut odit aut fugit, sed quia consequuntur</p>
  <p>Lorem ipsum dolor sit amet, consectetur adipiscing elit, sed do eiusmod tempor incididunt ut labore et dolore magna aliqua. Ut enim ad minim veniam, quis nostrud exercitation ullamco laboris nisi ut aliquip ex ea commodo consequat.</p>
  <span class="btn">Read More</span>
</section>

<section class="copy abs" style="left:100px;top:1748px;width:540px">
  <h2>Security Plus</h2>
  <p style="margin-bottom:0">Sed ut perspiciatis unde omnis iste natus error sit voluptatem accusantium doloreue laudtium, totam rem aperiam, eaque ipsa quae ab illo inventore veritatis et quasi architecto beatae vitae dicta sunt explicabo. Nemo enim ipsam voluptatem quia voluptas sit aspernatur</p>
  <ul class="checklist">
    <li><svg width="12" height="12" viewBox="0 0 12 12"><path d="m1 6 3.5 3.5L11 2" stroke="#d7242b" stroke-width="2" fill="none"/></svg>Cum sociis natoque penatibus et magnis</li>
    <li><svg width="12" height="12" viewBox="0 0 12 12"><path d="m1 6 3.5 3.5L11 2" stroke="#d7242b" stroke-width="2" fill="none"/></svg>Donec quam 100 % pellentesque</li>
    <li><svg width="12" height="12" viewBox="0 0 12 12"><path d="m1 6 3.5 3.5L11 2" stroke="#d7242b" stroke-width="2" fill="none"/></svg>Nulla consequat massa quis ulputate eget arcuin enim</li>
    <li><svg width="12" height="12" viewBox="0 0 12 12"><path d="m1 6 3.5 3.5L11 2" stroke="#d7242b" stroke-width="2" fill="none"/></svg>Donec pede justo fringilla vel aliquet justo</li>
  </ul>
  <span class="btn" style="width:126px;margin-top:0">Read More</span>
</section>
<div class="monitor-screen"><div role="img" aria-label="Hand operating a CCTV joystick controller in front of surveillance screens"></div></div>
<div class="monitor-chin"></div>
<div class="monitor-stand"></div>

<section class="blog">
  <h2 class="section-title">Latest Blog</h2>
  <article class="blog-card" style="left:100px">
    <div class="blog-thumb" role="img" aria-label="Technician installing a camera on a pole" style="background:linear-gradient(135deg,#6f7b55,#b7b9a6 50%,#8a6f4a)"></div>
    <div class="blog-body"><h4>Nemo enim ipsam voluptatem</h4><div class="blog-meta">◷ 3 minutes ago, 0 comments</div><p>Lorem ipsum dolor sit amet, consectetur adipiscing elit, sed do eiusmod tempor incididunt</p></div>
  </article>
  <article class="blog-card" style="left:444px">
    <div class="blog-thumb" role="img" aria-label="Camera watching a fuel station at sunset" style="background:linear-gradient(180deg,#8fa7c2,#e4b27f 55%,#8d8b87)"></div>
    <div class="blog-body"><h4>Nemo enim ipsam voluptatem</h4><div class="blog-meta">◷ 3 minutes ago, 0 comments</div><p>Lorem ipsum dolor sit amet, consectetur adipiscing elit, sed do eiusmod tempor incididunt</p></div>
  </article>
  <article class="blog-card" style="left:787px">
    <div class="blog-thumb" role="img" aria-label="Camera mounted outside a lit modern house at dusk" style="background:linear-gradient(135deg,#3b4f6b,#9aa7b8 45%,#e0b57a 70%,#5d5a52)"></div>
    <div class="blog-body"><h4>Nemo enim ipsam voluptatem</h4><div class="blog-meta">◷ 3 minutes ago, 0 comments</div><p>Lorem ipsum dolor sit amet, consectetur adipiscing elit, sed do eiusmod tempor incididunt</p></div>
  </article>
</section>

<footer class="site-footer">
  <div class="footer-col" style="left:100px;top:92px">
    <div class="brand" style="position:static"><span class="brand-mark"></span><span class="brand-name">Kestrel<br>Securities</span></div>
    <div class="socials"><span></span><span></span><span></span><span></span></div>
  </div>
  <div class="footer-col" style="left:358px;width:280px">
    <h4>Sign Up for Newsletter</h4>
    <p>Excepteur sint occaecat cupidatat non proident, sunt in culpa qui officia deserunt</p>
    <div class="newsletter-input">Enter email</div>
    <span class="btn newsletter-btn">Sign Up</span>
  </div>
  <div class="footer-col" style="left:686px;width:240px">
    <h4>Contact Us</h4>
    <div class="contact-line"><svg width="12" height="14" viewBox="0 0 12 16"><path d="M6 0a6 6 0 0 0-6 6c0 4.5 6 10 6 10s6-5.5 6-10a6 6 0 0 0-6-6zm0 8.5A2.5 2.5 0 1 1 6 3.5a2.5 2.5 0 0 1 0 5z" fill="#d7242b"/></svg><p>Kestrel Securities<br>240 Harbor Lane • Bayview, CA<br>90210</p></div>
    <div class="contact-line"><svg width="13" height="13" viewBox="0 0 24 24"><path fill="#d7242b" d="M6.6 10.8a15.1 15.1 0 0 0 6.6 6.6l2.2-2.2c.3-.3.7-.4 1-.2 1.1.4 2.3.6 3.6.6.6 0 1 .4 1 1V20c0 .6-.4 1-1 1A17 17 0 0 1 3 4c0-.6.4-1 1-1h3.5c.6 0 1 .4 1 1 0 1.3.2 2.5.6 3.6.1.3 0 .7-.2 1z"/></svg><p>Call &nbsp;+1 800 555 0142</p></div>
    <div class="contact-line"><svg width="13" height="11" viewBox="0 0 14 10"><rect width="14" height="10" fill="#d7242b"/><path d="m0 0 7 5 7-5" stroke="#fff" fill="none"/></svg><p>Email: info@kestrelsecurities.example</p></div>
  </div>
  <div class="footer-col" style="left:977px">
    <h4>Quick Links</h4>
    <ul class="quick-links"><li>Home</li><li>About Us</li><li>Our Services</li><li>Blog</li><li>Contact Us</li></ul>
  </div>
</footer>
<div class="footer-bar">© 2018 Kestrel Securities. - All rights reserved</div>

</body>
</html>
```